wine label for ultra premium vineyard in Bendigo, Central Otago, New Zealand

"LARKSPUR" is our new wine brand, with grapes grown in our spectacular "ter Hoeven" vineyard. The small, elevated vineyard overlooks a river valley and snowy mountains. We would like a highly elegant label for our 2018 pinot noir wine, which highlights the quality of wine and our very special vineyard location. "LARKSPUR" has to be prominent, with secondary emphasis on "ter Hoeven vineyard" and "Bendigo, Central Otago". A stylized LARKSPUR logo (bird) could be a useful design device instead of the commonly seen illustrated mountain landscape (which is quite common for our local wines). Label size 90 high, 110 wide. Please use a pinot noir / burgundy bottle. See here for vineyard pics, and also below pics for other local wine labels and pics for inspiration / styles. https://www.instagram.com/jas.ter.hoeven.example/

Target Market(s)

average bottle price for this premium red pinot noir would be aroundUS$40. target market are generally urban professionals aged 25 and older with a high degree of interest in pinot noir wine, and who are familiar with New Zealand pinot noir (ie. already know several brands).

Colors
ed252d

Requirements
Must have
• distinctive label, sophisticated look
Nice to have
• classy white paper stock
Should not have
• label must not get too busy... less but high quality and distinctive is more....

```html
<!DOCTYPE html>
<html lang="en">
<head>
<meta charset="utf-8">
<title>LARKSPUR – ter Hoeven vineyard Pinot Noir 2018 label</title>
<link href="https://fonts.googleapis.com/css2?family=Tenor+Sans&family=Montserrat:wght@400;500&display=swap" rel="stylesheet">
<style>
  :root {
    --backdrop: #ffffff;
    --paper: #fbfbfa;
    --paper-edge: #e4e4e1;
    --ink: #161616;
    --rule: #2a2a2a;
  }
  html, body {
    margin: 0;
    padding: 0;
    width: 851px;
    height: 1200px;
    overflow: hidden;
    background: var(--backdrop);
  }
  .canvas {
    position: relative;
    width: 851px;
    height: 1200px;
  }
  .label {
    position: absolute;
    left: 45px;
    top: 289px;
    width: 760px;
    height: 622px;
    background: var(--paper);
    box-shadow: inset 0 0 0 1px var(--paper-edge);
    color: var(--ink);
  }
  .brand {
    position: absolute;
    left: 231px;
    top: 142px;
    margin: 0;
    font-family: "Tenor Sans", sans-serif;
    font-weight: 400;
    font-size: 84px;
    line-height: 1;
    letter-spacing: 1px;
    width: 300px;
    text-align: left;
    white-space: nowrap;
  }
  .vineyard {
    position: absolute;
    left: 231px;
    top: 249px;
    width: 291px;
    border-top: 2px solid var(--rule);
    border-bottom: 1.5px solid var(--rule);
    padding: 7px 0 7px;
    font-family: "Montserrat", sans-serif;
    font-size: 19px;
    line-height: 1;
    text-align: center;
    letter-spacing: 0.3px;
  }
  .varietal {
    position: absolute;
    left: 0;
    right: 0;
    top: 492px;
    margin: 0;
    font-family: "Montserrat", sans-serif;
    font-weight: 500;
    font-size: 22px;
    text-align: center;
    letter-spacing: 0.5px;
  }
  .baseline-rule {
    position: absolute;
    left: 31px;
    right: 0;
    top: 566px;
    border-top: 1.5px solid var(--rule);
  }
  .brand-dot {
    position: absolute;
    left: 58px;
    top: 548px;
    width: 16px;
    height: 16px;
    border-radius: 50%;
    background: var(--ink);
  }
  .region {
    position: absolute;
    left: 64px;
    top: 586px;
    margin: 0;
    font-family: "Montserrat", sans-serif;
    font-weight: 500;
    font-size: 15px;
    letter-spacing: 0.2px;
  }
</style>
</head>
<body>
  <main class="canvas">
    <section class="label" aria-label="LARKSPUR Pinot Noir 2018 wine label">
      <h1 class="brand">LARKSPUR</h1>
      <div class="vineyard">ter Hoeven vineyard</div>
      <p class="varietal">Pinot Noir 2018</p>
      <span class="brand-dot" aria-hidden="true"></span>
      <div class="baseline-rule" aria-hidden="true"></div>
      <p class="region">Bendigo, Central Otago</p>
    </section>
  </main>
</body>
</html>
```